Custom Cabinet Shop Needs a website design

Hi,
We need a website for a Custom Cabinet Shop and Cabinet parts manufacturing business.
The business has two sides to it. One side provides custom Kitchens, vanities, entertainment units, offices and what not to homeowners and contractors.
The 2nd side of the business provides built to order cabinet boxes and other parts required to put together a project to other cabinet shops, small contractors looking to install there own cabinets.
Website will need a Gallery to display work.
Color scheme to go well with logo.
current website is www.brindlewoodcustomcabinets.com
being changed to www.brindlewood.ca
Logo Included in attached files.
Tagline "Millwork with Flare"
Mission Statement "Our passion is to deliver inspired cabinetry solutions to suit all your needs, supported by our phenomenal star class customer service"
The website should convey quality and professionalism.
Thank you.
Homeowners/ Contractors
Entertainment
Coded - Design and coding required
1 page

```html
<!DOCTYPE html>
<html lang="en">
<head>
<meta charset="utf-8">
<title>Brindlewood Custom Cabinets</title>
<link rel="stylesheet" href="https://fonts.googleapis.com/css2?family=Lato:wght@300;400;700;900&display=swap">
<style>
  :root {
    --orange: #e8561c;
    --ink: #0a0a0a;
    --text: #222222;
    --muted: #555555;
    --rule: #d6d6d6;
    --footer-bg: #ececec;
    --white: #ffffff;
  }
  * { margin: 0; padding: 0; box-sizing: border-box; }
  html, body { width: 1120px; height: 1200px; overflow: hidden; background: var(--white); }
  body { position: relative; font-family: "Lato", sans-serif; color: var(--text); }

  .site-header { position: absolute; left: 0; top: 0; width: 1120px; height: 110px; }
  .brand { position: absolute; display: flex; align-items: center; gap: 8px; }
  .brand-mark { width: 14px; height: 14px; background: var(--orange); }
  .brand-name { font-weight: 900; font-size: 20px; letter-spacing: 1px; color: var(--ink); }
  .site-header .brand { left: 162px; top: 42px; }

  .main-nav { position: absolute; left: 397px; top: 32px; display: flex; }
  .main-nav a {
    width: 112px; height: 44px; display: flex; align-items: center; justify-content: center;
    border-left: 1px solid var(--rule); font-size: 11px; color: var(--text); text-decoration: none;
  }
  .main-nav a.is-active { color: var(--orange); }

  .hero {
    position: absolute; left: 0; top: 110px; width: 1120px; height: 586px;
    background: linear-gradient(100deg, #1d2733 0%, #3a3026 30%, #8a5a2c 60%, #a0703e 80%, #6e5a48 100%);
  }
  .hero-caption {
    position: absolute; left: 298px; top: 235px; width: 528px; height: 119px;
    background: rgba(0,0,0,0.92);
    box-shadow: 4px 4px 0 var(--orange);
    display: flex; align-items: center; justify-content: center;
    font-weight: 300; font-size: 38px; letter-spacing: 4px; color: var(--white);
    padding-bottom: 24px;
  }
  .hero-caption .accent { color: var(--orange); margin-right: 14px; }
  .hero-dots { position: absolute; left: 513px; top: 542px; display: flex; gap: 9px; }
  .hero-dots span { width: 12px; height: 12px; border-radius: 50%; border: 1.5px solid var(--white); }
  .hero-dots span.is-current { background: var(--white); }

  .mission { position: absolute; left: 0; top: 740px; width: 1120px; text-align: center; }
  .mission h2 { font-weight: 900; font-size: 32px; letter-spacing: 3px; color: var(--ink); line-height: 1; }
  .mission-rule { display: block; width: 109px; height: 7px; margin: 21px auto 0; background: var(--ink); box-shadow: 3px 3px 0 var(--orange); }
  .mission p { margin-top: 21px; font-weight: 300; font-size: 19px; letter-spacing: 1.5px; line-height: 29px; color: var(--text); }
  .btn-work {
    display: inline-flex; align-items: center; justify-content: center;
    margin-top: 28px; width: 157px; height: 45px; background: var(--ink); color: var(--white);
    font-weight: 700; font-size: 13px; letter-spacing: 1.5px; text-decoration: none;
    box-shadow: 3px 3px 0 var(--orange);
  }

  .site-footer { position: absolute; left: 0; top: 1050px; width: 1120px; height: 150px; background: var(--footer-bg); border-top: 1px solid #333; }
  .footer-nav { position: absolute; left: 162px; top: 36px; display: flex; font-size: 11px; }
  .footer-nav a { color: var(--text); text-decoration: none; }
  .footer-nav .sep { color: #999; margin: 0 12px; }
  .footer-contact { position: absolute; left: 162px; top: 67px; display: flex; align-items: center; font-size: 13px; color: var(--orange); }
  .footer-contact .icon { width: 15px; height: 15px; margin-right: 6px; }
  .footer-contact .item { display: flex; align-items: center; margin-right: 10px; }
  .social { display: flex; gap: 3px; margin-left: -4px; }
  .social span { width: 18px; height: 18px; border-radius: 50%; background: var(--ink); }
  .copyright { position: absolute; left: 162px; top: 97px; font-size: 11px; color: var(--muted); }
  .site-footer .brand { left: 770px; top: 48px; }
</style>
</head>
<body>
  <header class="site-header">
    <div class="brand"><span class="brand-mark"></span><span class="brand-name">BRINDLEWOOD</span></div>
    <nav class="main-nav">
      <a class="is-active" href="#">HOME</a>
      <a href="#">GALLERY</a>
      <a href="#">SERVICES</a>
      <a href="#">WARRANTY</a>
      <a href="#">CONTACT</a>
    </nav>
  </header>

  <section class="hero" role="img" aria-label="Photo of a custom basement bar with dark cabinets, stone-clad counter, pendant lights and leather bar stools">
    <div class="hero-caption"><span class="accent">MILLWORK</span>WITH FLARE</div>
    <div class="hero-dots"><span class="is-current"></span><span></span><span></span><span></span><span></span></div>
  </section>

  <section class="mission">
    <h2>OUR MISSION</h2>
    <span class="mission-rule"></span>
    <p>Our passion is to deliver inspired cabinetry solutions to suit all your needs,<br>supported by our phenomenal star class customer service</p>
    <a class="btn-work" href="#">VISIT OUR WORK</a>
  </section>

  <footer class="site-footer">
    <nav class="footer-nav">
      <a href="#">HOME</a><span class="sep">|</span>
      <a href="#">GALLERY</a><span class="sep">|</span>
      <a href="#">SERVICES</a><span class="sep">|</span>
      <a href="#">WARRANTY</a><span class="sep">|</span>
      <a href="#">CONTACT</a>
    </nav>
    <div class="footer-contact">
      <span class="item">
        <svg class="icon" viewBox="0 0 16 16"><circle cx="8" cy="8" r="8" fill="#e8561c"/><path d="M5 4.2l1.6-.4 1 2.2-1 .8c.5 1.1 1.3 1.9 2.4 2.4l.8-1 2.2 1-.4 1.6c-3.4.2-6.8-3.2-6.6-6.6z" fill="#fff"/></svg>
        403-555-0187
      </span>
      <span class="item">
        <svg class="icon" viewBox="0 0 16 16"><circle cx="8" cy="8" r="8" fill="#e8561c"/><rect x="4" y="5" width="8" height="6" fill="#fff"/><path d="M4 5l4 3.2L12 5" stroke="#e8561c" stroke-width="1" fill="none"/></svg>
        sales@brindlewoodcustomcabinets.com
      </span>
      <span class="social"><span></span><span></span><span></span></span>
    </div>
    <p class="copyright">©copyright 2015. All rights reserved</p>
    <div class="brand"><span class="brand-mark"></span><span class="brand-name">BRINDLEWOOD</span></div>
  </footer>
</body>
</html>
```